Tovin Marsk Technologies Web Site

I need website designed for Tovin Marsk Technologies, LLC. It is an email marketing software as a service business. I am looking for a five page website with the ability to accept payments. I have included our logo below for integration with the website. I do not have the text ready yet.

The domain to use is tovin-marsk.com

I have also included some examples of other websites that outline the basic structure I would like
https://trybluvesto.com/
https://www.postvaro.com/

I know I need to provide some more information, but I want to get the ball rolling and see what is needed.
Thanks!
Eli

```html
<!DOCTYPE html>
<html lang="en">
<head>
<meta charset="utf-8">
<title>Tovin Marsk Technologies — Better Email Marketing</title>
<link href="https://fonts.googleapis.com/css2?family=Montserrat:ital,wght@0,400;0,500;0,600;0,700;1,400&display=swap" rel="stylesheet">
<style>
:root{
  --blue-deep:#3a2ce6;
  --blue-bright:#1d8be2;
  --red:#e8232a;
  --ink:#1f2230;
  --muted:#6b6f7c;
  --line:#e4e6ec;
  --soft:#f6f7f9;
  --pale-blue:#eef5fd;
  --white:#ffffff;
}
*{box-sizing:border-box;margin:0;padding:0}
html,body{width:1200px;height:4286px;overflow:hidden}
body{position:relative;background:var(--white);font-family:"Montserrat",sans-serif;color:var(--ink)}
.abs{position:absolute}
.btn{position:absolute;display:flex;align-items:center;justify-content:center;border-radius:20px;font-size:12px;font-weight:600;text-decoration:none}
.btn-red{background:var(--red);color:var(--white);box-shadow:0 6px 14px rgba(232,35,42,.3)}
.btn-ghost{border:2px solid var(--white);color:var(--white)}
.placeholder{position:absolute;border-radius:10px}
.square{position:absolute;border-radius:4px}

/* hero */
.hero{position:absolute;left:0;top:0;width:1200px;height:491px;background:linear-gradient(90deg,var(--blue-deep),var(--blue-bright));overflow:hidden}
.brand{position:absolute;left:140px;top:24px;display:flex;align-items:center;gap:10px;color:var(--white);font-weight:700;font-size:15px;letter-spacing:1px}
.brand-dot{width:34px;height:34px;border-radius:50%;background:var(--white)}
.nav{position:absolute;left:430px;top:34px;display:flex;gap:44px;color:var(--white);font-size:12px;font-weight:600}
.nav-login{left:900px;top:28px;width:64px;height:28px;border-radius:4px;border:1.5px solid var(--white);font-size:11px}
.nav-signup{left:980px;top:28px;width:70px;height:28px;border-radius:4px;font-size:11px}
.hero-title{position:absolute;left:0;width:1200px;top:108px;text-align:center;color:var(--white);font-size:44px;font-weight:500;letter-spacing:1px}
.hero-sub{position:absolute;left:0;width:1200px;top:162px;text-align:center;color:var(--white);font-size:22px;font-weight:500;letter-spacing:3px}

/* features */
.feature-title{position:absolute;font-size:28px;font-weight:500;line-height:38px}
.feature-text{position:absolute;font-size:14px;line-height:25px;color:#3a3d48}
.brand-row{position:absolute;display:flex;gap:34px;font-size:20px;font-weight:600;color:#c9ccd4}
.quote{position:absolute;font-size:14px;line-height:25px;font-style:italic;color:var(--muted)}
.author-name{position:absolute;font-size:11px;font-weight:700;letter-spacing:.5px}
.author-role{position:absolute;font-size:10px;color:var(--muted)}

/* pricing */
.pricing{position:absolute;left:0;top:2186px;width:1200px;height:380px;background:var(--soft)}
.center{position:absolute;left:0;width:1200px;text-align:center}

/* faq */
.faq-tabs{position:absolute;left:370px;top:2690px;width:460px;display:flex;justify-content:space-between;font-size:12px;font-weight:600;color:var(--muted)}
.faq-tabs .active{color:var(--ink);border-bottom:3px solid #2e6ae6;padding-bottom:8px}
.faq-rule{position:absolute;left:370px;top:2718px;width:460px;height:1px;background:var(--line)}
.faq-item{position:absolute;left:200px;width:800px;height:62px;border-bottom:1px solid var(--line);display:flex;align-items:center;justify-content:space-between;font-size:14px;padding:0 2px}
.faq-item.open{font-weight:600}
.faq-toggle{width:18px;height:18px;border-radius:50%;background:#eceef2;display:flex;align-items:center;justify-content:center;font-size:13px;font-weight:600;color:var(--ink)}
.faq-answer{position:absolute;left:200px;top:2880px;width:800px;height:110px;background:var(--pale-blue);padding:18px 22px;font-size:12px;line-height:22px;color:#3a3d48}

/* partners */
.partners{position:absolute;left:0;top:3286px;width:1200px;height:320px;background:linear-gradient(90deg,var(--blue-deep),var(--blue-bright));overflow:hidden}
.partner-badge{position:absolute;top:124px;width:180px;height:80px;background:var(--white);border-radius:4px;display:flex;align-items:center;justify-content:center;font-size:18px;font-weight:600;color:#8a8e99}
.dots{position:absolute;display:flex;gap:8px}
.dots span{width:6px;height:6px;border-radius:50%;background:rgba(255,255,255,.6)}

/* testimonials */
.testimonials{position:absolute;left:0;top:3606px;width:1200px;height:394px;background:#f2f3f6}
.testi-card{position:absolute;top:65px;width:314px;height:130px;background:var(--white);border-radius:6px;box-shadow:0 6px 18px rgba(0,0,0,.06);padding:24px 26px;font-size:11px;line-height:18px;text-align:center;color:#3a3d48}
.testi-mark{display:block;color:#2e6ae6;font-size:22px;font-weight:700;line-height:16px;margin-top:2px}
.testi-name{position:absolute;top:250px;text-align:right;font-size:11px;font-weight:700}
.testi-name small{display:block;font-weight:400;color:var(--muted);font-size:10px}
.avatar{position:absolute;border-radius:50%;background:linear-gradient(135deg,#b9bcc6,#7f8390)}
.arrow{position:absolute;top:180px;color:#2e6ae6;font-size:26px;font-weight:600}

/* footer */
.footer{position:absolute;left:0;top:4000px;width:1200px;height:286px}
.newsletter-label{position:absolute;left:190px;top:38px;font-size:12px;line-height:16px}
.newsletter-label b{font-weight:600;font-size:14px}
.field{position:absolute;top:44px;height:32px;border:1px solid #d6d8de;border-radius:3px;font-size:11px;color:var(--muted);padding:0 10px;display:flex;align-items:center}
.subscribe{left:870px;top:44px;width:120px;height:32px;border-radius:3px;font-size:11px}
.foot-contact{position:absolute;left:190px;font-size:11px;color:var(--ink);display:flex;align-items:center;gap:8px}
.foot-col{position:absolute;top:112px;font-size:11px;line-height:18px;color:#3a3d48}
.foot-col h4{font-size:13px;font-weight:600;color:var(--ink);margin-bottom:6px}
</style>
</head>
<body>

<header class="hero">
  <div class="square" style="left:420px;top:130px;width:70px;height:70px;background:rgba(255,255,255,.08);transform:rotate(20deg)"></div>
  <div class="square" style="left:1060px;top:90px;width:90px;height:90px;background:rgba(255,255,255,.08);transform:rotate(-15deg)"></div>
  <div class="square" style="left:60px;top:230px;width:60px;height:60px;background:rgba(255,255,255,.07);transform:rotate(30deg)"></div>
  <div class="square" style="left:1020px;top:280px;width:70px;height:70px;background:rgba(255,255,255,.07);transform:rotate(10deg)"></div>
  <div class="brand"><span class="brand-dot"></span>TOVIN MARSK</div>
  <nav class="nav"><span>Pricing</span><span>About us</span><span>Contact</span><span>Blog</span><span>FAQs</span></nav>
  <a class="btn nav-login" style="color:var(--white)">Login</a>
  <a class="btn btn-red nav-signup">Sign up</a>
  <h1 class="hero-title">BETTER EMAIL MARKETING</h1>
  <p class="hero-sub">Easier like never before start now</p>
  <a class="btn btn-red" style="left:458px;top:228px;width:136px;height:40px">Get Started</a>
  <a class="btn btn-ghost" style="left:630px;top:228px;width:120px;height:40px">See Pricing</a>
</header>

<div class="placeholder" role="img" aria-label="Laptop showing the email marketing analytics dashboard" style="left:270px;top:314px;width:660px;height:376px;background:linear-gradient(180deg,#f4f6fa,#d9dee8)"></div>
<div class="square" style="left:346px;top:316px;width:54px;height:54px;background:#2a40e6;transform:rotate(15deg)"></div>
<div class="square" style="left:730px;top:464px;width:54px;height:54px;background:var(--red);transform:rotate(20deg)"></div>
<div class="square" style="left:340px;top:530px;width:30px;height:30px;background:var(--red);transform:rotate(-20deg)"></div>
<div class="square" style="left:910px;top:512px;width:44px;height:44px;background:#2a40e6;transform:rotate(18deg)"></div>

<!-- editor feature -->
<div class="placeholder" role="img" aria-label="Illustration of a drag-and-drop email editor" style="left:257px;top:800px;width:343px;height:243px;background:linear-gradient(135deg,#eef3fb,#d6e4f6)"></div>
<h2 class="feature-title" style="left:643px;top:828px">Where Teams Create and<br>Send Beautiful Emails</h2>
<div class="brand-row" style="left:643px;top:920px"><span>Cartwell</span><span>Shopnest</span><span>Chatterly</span></div>
<p class="feature-text" style="left:643px;top:970px;width:400px">Our intuitive drag-and-drop editor makes designing the perfect email faster with real-time collaboration and in-app commenting</p>
<a class="btn btn-red" style="left:635px;top:1084px;width:122px;height:38px">Get Started</a>
<div class="square" style="left:1080px;top:836px;width:14px;height:14px;background:var(--red)"></div>
<div class="square" style="left:320px;top:1234px;width:16px;height:16px;background:#2a40e6"></div>
<div class="square" style="left:808px;top:1206px;width:12px;height:12px;background:#2a40e6"></div>

<!-- targeting feature -->
<div class="placeholder" style="left:840px;top:1280px;width:360px;height:380px;background:var(--pale-blue);border-radius:200px 0 0 200px"></div>
<h2 class="feature-title" style="left:171px;top:1345px">Target specific contacts<br>collobare with team!</h2>
<p class="feature-text" style="left:171px;top:1428px;width:380px">A big part of our email marketing process is validation and nailing the details. Tovin Marsk lets us iterate quickly, elevate quality.</p>
<a class="btn btn-red" style="left:171px;top:1552px;width:122px;height:38px">Get Started</a>
<div class="placeholder" role="img" aria-label="Dashboard screens showing campaign charts and a world map" style="left:606px;top:1340px;width:551px;height:236px;background:linear-gradient(135deg,#f2f5fa,#d7dfec)"></div>
<div class="square" style="left:526px;top:1652px;width:20px;height:20px;background:var(--red)"></div>
<div class="square" style="left:96px;top:1674px;width:14px;height:14px;background:#2a40e6"></div>
<div class="square" style="left:1030px;top:1732px;width:20px;height:20px;background:#2a40e6"></div>

<!-- feedback feature -->
<div class="placeholder" role="img" aria-label="Hand holding a phone showing a campaign checklist" style="left:129px;top:1786px;width:442px;height:400px;background:linear-gradient(135deg,#eef1f6,#d5dbe6)"></div>
<h2 class="feature-title" style="left:623px;top:1812px">Our good feedbacks and<br>statistics shows all</h2>
<p class="quote" style="left:623px;top:1890px;width:380px">“A big part of our design process is validation and nailing the details. Tovin Marsk lets us iterate quickly, elevate quality, and do it fast.”</p>
<div class="abs" style="left:940px;top:1948px;font-size:60px;font-weight:700;color:#d3d6dd;line-height:60px">”</div>
<div class="avatar" role="img" aria-label="Portrait of Dario Velmont" style="left:623px;top:2000px;width:48px;height:48px;background:#e6e8ed"></div>
<div class="author-name" style="left:685px;top:2012px">DARIO VELMONT</div>
<div class="author-role" style="left:685px;top:2028px">CORVANE, CEO</div>
<a class="btn btn-red" style="left:623px;top:2082px;width:122px;height:38px">Get Started</a>
<div class="square" style="left:580px;top:1950px;width:14px;height:14px;background:#2a40e6"></div>
<div class="square" style="left:1006px;top:2104px;width:12px;height:12px;background:#2a40e6"></div>

<!-- pricing -->
<section class="pricing">
  <div class="abs" style="left:570px;top:52px;width:60px;height:60px;border-radius:50%;background:#2a40e6"></div>
  <p class="center" style="top:150px;font-size:24px;font-weight:400">Grab Our Plan This Weekend</p>
  <p class="center" style="top:184px;font-size:46px;font-weight:600">$19,99 / month</p>
  <a class="btn btn-red" style="left:508px;top:270px;width:184px;height:42px;font-size:13px">Check Plans</a>
</section>

<!-- faq -->
<h2 class="center" style="top:2628px;font-size:28px;font-weight:500;letter-spacing:1px">FREQUENTLY ASKED QUESTIONS</h2>
<div class="faq-rule"></div>
<div class="faq-tabs"><span class="active">PRICING</span><span>DISCOUNTS</span><span>HOW IT WORKS</span><span>MOBILE</span></div>
<div class="faq-item" style="top:2754px">Answer for a way way longer question with longer answer<span class="faq-toggle">+</span></div>
<div class="faq-item open" style="top:2816px;border-bottom:none">Answer for some kind of question<span class="faq-toggle">−</span></div>
<div class="faq-answer">Our plans bill monthly or yearly, and you may switch or cancel at any time from your account page. Yearly plans save twenty percent, include priority support, and keep every template, contact list and report you have built. Discounts apply automatically at checkout when a promo code is entered.</div>
<div class="faq-item" style="top:3004px">How much cost your plant to buy for a year?<span class="faq-toggle">+</span></div>
<div class="faq-item" style="top:3072px">Do you have something like free trial for this program?<span class="faq-toggle">+</span></div>
<div class="faq-item" style="top:3140px">Where I can find you in a local place?<span class="faq-toggle">+</span></div>

<!-- partners -->
<section class="partners">
  <div class="square" style="left:120px;top:180px;width:70px;height:70px;background:rgba(255,255,255,.08);transform:rotate(20deg)"></div>
  <div class="square" style="left:1040px;top:40px;width:80px;height:80px;background:rgba(255,255,255,.08);transform:rotate(-15deg)"></div>
  <h2 class="center" style="top:50px;color:var(--white);font-size:34px;font-weight:500">Our Partners</h2>
  <div class="partner-badge" style="left:200px">Fundlaunch</div>
  <div class="partner-badge" style="left:400px">Cartwell</div>
  <div class="partner-badge" style="left:600px">Shopnest</div>
  <div class="partner-badge" style="left:800px">Chatterly</div>
  <div class="dots" style="left:570px;top:246px"><span></span><span></span><span style="background:var(--white)"></span><span></span></div>
</section>

<!-- testimonials -->
<section class="testimonials">
  <div class="arrow" style="left:44px">‹</div>
  <div class="arrow" style="left:1136px">›</div>
  <div class="testi-card" style="left:108px">Setting up campaigns took minutes, and our open rates grew within the first month of sending.<span class="testi-mark">”</span></div>
  <div class="testi-card" style="left:436px">Setting up campaigns took minutes, and our open rates grew within the first month of sending.<span class="testi-mark">”</span></div>
  <div class="testi-card" style="left:766px">Setting up campaigns took minutes, and our open rates grew within the first month of sending.<span class="testi-mark">”</span></div>
  <div class="testi-name" style="left:160px;width:110px">Nils Ardent CEO<small>Company Name</small></div>
  <div class="avatar" role="img" aria-label="Customer portrait" style="left:278px;top:238px;width:52px;height:52px"></div>
  <div class="testi-name" style="left:490px;width:110px">Nils Ardent CEO<small>Company Name</small></div>
  <div class="avatar" role="img" aria-label="Customer portrait" style="left:608px;top:238px;width:52px;height:52px"></div>
  <div class="testi-name" style="left:820px;width:110px">Nils Ardent CEO<small>Company Name</small></div>
  <div class="avatar" role="img" aria-label="Customer portrait" style="left:938px;top:238px;width:52px;height:52px"></div>
  <div class="dots" style="left:552px;top:330px"><span style="background:#c9ccd4"></span><span style="background:#c9ccd4"></span><span style="background:#2e6ae6"></span><span style="background:#c9ccd4"></span><span style="background:#c9ccd4"></span></div>
</section>

<!-- footer -->
<footer class="footer">
  <p class="newsletter-label">Subscribe<br><b>For Our Newsletter</b></p>
  <div class="field" style="left:420px;width:140px">Full Name...</div>
  <div class="field" style="left:575px;width:230px">Email Address...</div>
  <a class="btn btn-red subscribe">Subscribe</a>
  <div class="abs" style="left:190px;top:102px;width:62px;height:62px;border-radius:50%;background:#2a40e6"></div>
  <div class="foot-contact" style="top:178px">
    <svg width="12" height="12" viewBox="0 0 12 12"><path d="M2 1h2.5l1 3-1.5 1a6 6 0 0 0 3 3l1-1.5 3 1V10a1 1 0 0 1-1 1A9 9 0 0 1 1 2a1 1 0 0 1 1-1z" fill="#2a40e6"/></svg>+1 555 014 0283</div>
  <div class="foot-contact" style="top:198px">
    <svg width="12" height="12" viewBox="0 0 12 12"><rect x="1" y="2.5" width="10" height="7" rx="1" fill="none" stroke="#2a40e6" stroke-width="1.4"/><path d="M1.5 3l4.5 3.5L10.5 3" fill="none" stroke="#2a40e6" stroke-width="1.4"/></svg>info@tovin-marsk.com</div>
  <div class="foot-col" style="left:420px"><h4>About Tovin Marsk</h4>Newsletter<br>Our Memberships<br>Events<br>Investors<br>Supplier Response</div>
  <div class="foot-col" style="left:650px"><h4>Account</h4>Manage Your ID<br>Tovin Marsk Store<br>Customer Review<br>Ask a Question<br>Why choose us?</div>
  <div class="foot-col" style="left:870px"><h4>More</h4>Inclusion and Diversity<br>Supplier Responsibility<br>Inclusion and Diversity<br>Shop for Business<br>Shop for Consumers</div>
</footer>

</body>
</html>
```